依頼詳細
概要、特徴にも書いたように、今回、分離発注に向けた営業用のチラシを作成して頂きたいです。

・すでに既存で新規顧客獲得用のパンフレット(高難度松浦工業)とチラシ(HARUKAZE)があり、今回は、それらに追加で挟む “分離発注を目的としたチラシ” の依頼となります。

※既存(高難度パンフレット)(添付資料1、2)
+
既存(HARUKAZE)(添付資料3)
+
“分離発注を目的としたチラシ”

既存の3つのチラシ(※添付資料1.2.3)と一緒に挟んで、配布したいので

流れを理解して作成していただけたら幸いです。

・流れ、
株式会社松浦工業は、高難度の足場を専門で営業しています。

また、その職人で構成されている、HARUKAZEというワンランク上の足場サービスも運営しています。(住人さんや近隣様、などへの配慮、最高のサービスを提供するブランド)
(HARUKAZEにもホームページがございます。)

安全には、費用がかかります。
人の命は尊いです。
工事は足場から始まり、足場で終わります。
そして、業者みんなが使う足場です。

弊社の売りを武器として運営し維持して行くためには、無駄な予算を削り、その予算を安心できる工事に生かす。

そして見た目も美しい職人で揃えている私たちと手を組みませんか。

。。。といった流れでイメージして作成して頂きたいです。

※弊社の売りに関しましては、添付した資料やホームページを確認して頂き、理解して頂きたいです。

・目的は、新規顧客の獲得ですが、分離発注の提案を載せたいです。

・新規顧客(ターゲット)→ビル建物のオーナー、元請業社、ゼネコンなど

・メリットとデメリットをまとめたマインドマップも添付しますので、必要であれば使ってください。
・他にも、ホームページもありますので、見ていただけたら、と思います。
・弊社は改修工事用の足場をメインで運営しております。
(居住者様や、近隣様、歩行者様からの安心や業者間、現場管理監督様とのコミュニケーションもとても大切にしております。)
・メリットのマインドマップの他にも、弊社を使うことでのメリットは、たくさんあります。
・どの立場から見ても美しい足場屋を目指しております。

記載項目
分離発注しませんか。

株式会社松浦工業
042−718−2964
https://matsuurakogyo-ashiba.example
↑↑
株式会社松浦工業(高難度専門の足場サービス)

https://harukaze-ashiba.example
↑↑
ワンランク上の足場サービス
HARUKAZE ホームページ

サイズ
A4
ページ数
両面
希望イメージ
シンプル 複雑
単色 カラフル
暗い 明るい
日常 高級
遊び心 厳粛
未来的 伝統的
女性的 男性的
希望する色
黄・オレンジ系、緑系、青系、既存チラシ(添付資料1.2.3)とのバランスで決めて頂きたい
納品ファイル
• 高解像度JPG (.jpg)
• イラストレーター形式 (.ai)
補足説明
↑↑
株式会社松浦工業(高難度専門の足場サービス)

↑↑
ワンランク上の足場サービス
HARUKAZE ホームページ

どちらも並行して運営しております!

ーーーーーーーーーーーーーーーーーーーーーーーーー

※多少の文字の変更などがしやすいように、アウトライン化されていないデータでも納品して頂きたいです。
みなさま、すばらしい作品をありがとうございます!

みなさまの作品を見て間違えに気づくことが出来ました。

一部、変更させてください!

3点あるのですが、

①1つ目は、このチラシを誰に当てた手紙にするのか、ですが、ターゲットは、
・ビルやマンション、学校など建物のオーナー様
・ビルやマンションの管理をしている管理会社様や、
・不動産会社様
・店舗、等の工事担当者様
に当てた手紙で作成して頂きたいです。

※よく考えたら工事会社が直接足場屋に依頼するのは、当前のことだと思いましたので、工事業者に当てるのはおかしい話だと気付いたので宜しくお願いいたします。

②見積もり依頼までの流れを盛り込んで頂きたいです。
流れ
平日の9:00〜17:00に
042−718−2964

に電話をして頂き、弊社の電話に出た物に、見積もりして欲しい物件のご住所をお聞かせください。

or

当社ホームページ問い合わせフォームのQRコード?
かURL??

で見積もり依頼のメッセージを頂けたら、

1週間以内にTerravue Mapsを元に概算でお見積もりして郵送させて頂きます。

※建物の改修工事が決まりましたら、弊社と工事業者様とで直接お打ち合わせして、施工します!
※安心、安全へのクオリティは、高品質をお約束しますので、安心してください。
※足場工事は、命の危険を伴う工事です。

。。。のような感じをうまく刺さる形で表現して頂きたいです。

③ターゲットに分離発注という意味を理解してもらえるのかも不安になってきたのですが、どうでしょうか。

このチラシに足場だけを分離発注しませんか?なのか、
直接発注しませんか、なのか、何か良い表現があればそれも考えていただけると幸いです。

分離発注でわかるから大丈夫だよ、であれば分離発注も構いません。
ただ僕が不安になっただけなので、
そこも何か良い案があればなーと思ったので、宜しくお願いいたします。

コロナで、大ダメージを受けてしまったので、これで、復活したいと考えております!

みなさま、どうか宜しくお願いいたします!

弊社の既存のパンフレットと一緒に配ることを踏まえてこの作品が一番良いのではないかと感じました。

この度は、本当にありがとうございました。
僕たちは、職人さん達の生活がもっと潤っていけるように、したいと考えております。
職人さん達の世界では土曜も仕事をすることが当たり前となっております。
しかし僕たちは価値の高い仕事を社会に広めていき、みんなが、より良い工事をしながら、生活も潤っていけるように考えております。
皆さんが作ってくれた作品から、僕たちは大きな気づきをゲットしました!
とても感謝しています。
本当に本当にありがとうございました。

```html
<!DOCTYPE html>
<html lang="ja">
<head>
<meta charset="UTF-8">
<title>分離発注しませんか？ — 松浦工業 / HARUKAZE</title>
<link rel="stylesheet" href="https://fonts.googleapis.com/css2?family=Noto+Serif+JP:wght@500;700&family=Noto+Sans+JP:wght@400;700;900&display=swap">
<style>
  :root {
    --paper: #ffffff;
    --ink: #2a2a2a;
    --navy-deep: #0b1533;
    --navy: #13245a;
    --blue: #1f4fa8;
    --blue-bright: #2d63c4;
    --gold: #c9a24a;
    --steel-light: #e6e8ec;
    --steel: #b9bec7;
    --stage: #eeeeee;
  }
  * { box-sizing: border-box; margin: 0; padding: 0; }
  html, body { width: 849px; height: 1200px; overflow: hidden; background: var(--stage); }
  .flyer {
    position: relative;
    width: 849px; height: 1200px;
    background: var(--paper);
    overflow: hidden;
    font-family: "Noto Sans JP", sans-serif;
    color: var(--ink);
  }
  .brand-tag {
    position: absolute; top: 30px; left: 34px;
    display: flex; align-items: center; gap: 6px;
    font-size: 12px; font-weight: 700; color: var(--blue);
  }
  .brand-tag .mark { width: 14px; height: 14px; background: var(--blue); }

  .headline {
    position: absolute; top: 48px; left: 328px;
    writing-mode: vertical-rl;
    font-family: "Noto Serif JP", serif;
    font-weight: 500;
    font-size: 56px;
    line-height: 1.28;
    letter-spacing: 0.04em;
    color: var(--ink);
  }

  .visual { position: absolute; border-radius: 2px; }
  .visual.ladder {
    left: 78px; top: 190px; width: 140px; height: 560px;
    background: linear-gradient(180deg, var(--steel-light), var(--steel));
  }
  .visual.frame {
    left: 320px; top: 500px; width: 150px; height: 220px;
    background: linear-gradient(180deg, var(--steel-light), var(--steel));
  }
  .visual.pipes {
    left: 612px; top: 50px; width: 110px; height: 610px;
    background: linear-gradient(180deg, var(--steel-light), var(--steel));
  }

  .lower {
    position: absolute; left: 0; top: 740px; width: 849px; height: 460px;
    background: linear-gradient(180deg, var(--navy) 0%, var(--navy-deep) 60%, #070d22 100%);
  }
  .lower .site-photo {
    position: absolute; inset: 80px 0 0 0;
    background: linear-gradient(160deg, rgba(45,99,196,0.35) 0%, rgba(11,21,51,0.2) 50%, rgba(201,162,74,0.18) 100%);
  }
  .callout {
    position: absolute; left: 0; top: 0; width: 100%; height: 80px;
    background: linear-gradient(90deg, var(--blue) 0%, var(--blue-bright) 50%, var(--blue) 100%);
    display: flex; align-items: center; justify-content: center;
    color: #fff; font-weight: 900; font-size: 42px; letter-spacing: 0.06em;
  }
  .company {
    position: absolute; left: 60px; top: 130px; width: 300px;
    color: #fff; text-align: center;
  }
  .company .lead { font-size: 22px; font-weight: 700; text-align: left; letter-spacing: 0.04em; }
  .company .name {
    margin-top: 60px; display: flex; align-items: center; justify-content: center; gap: 12px;
    font-size: 30px; font-weight: 700; letter-spacing: 0.1em;
  }
  .company .name .dot { width: 26px; height: 26px; border-radius: 50%; background: #fff; }

  .service {
    position: absolute; right: 60px; top: 140px; width: 330px; text-align: center;
  }
  .service .name {
    display: flex; align-items: center; justify-content: center; gap: 12px;
    font-size: 34px; font-weight: 700; letter-spacing: 0.12em; color: var(--gold);
  }
  .service .name .box { width: 28px; height: 28px; background: var(--gold); }
  .service .tagline {
    margin-top: 90px; padding: 10px 0;
    background: rgba(7,13,34,0.85);
    color: #fff; font-size: 24px; font-weight: 700; letter-spacing: 0.06em;
  }
</style>
</head>
<body>
<main class="flyer">
  <div class="brand-tag"><span class="mark"></span>松浦工業</div>

  <div class="visual ladder" role="img" aria-label="仮設足場のはしごのイラスト"></div>
  <div class="visual frame" role="img" aria-label="足場の枠組み部材のイラスト"></div>
  <div class="visual pipes" role="img" aria-label="足場の単管パイプのイラスト"></div>

  <h1 class="headline">発注も工事施工も<br>ぐっと、もっと、<br>スマートに。</h1>

  <section class="lower">
    <div class="site-photo" role="img" aria-label="夜の現場に組まれた仮設足場の写真"></div>
    <h2 class="callout">分離発注しませんか？</h2>

    <div class="company">
      <p class="lead">高難度の仮設足場専門</p>
      <p class="name"><span class="dot"></span>MATSUURA</p>
    </div>

    <div class="service">
      <p class="name"><span class="box"></span>HARUKAZE</p>
      <p class="tagline">仮設足場の高品質サービス</p>
    </div>
  </section>
</main>
</body>
</html>
```